Banner for back of trucks

We make a product that is called "Brindo".
It attaches to the side of hay balers and automatically applies tags to bales as they are being made.
We require a simple / modern banner design that will be affixed to the back of hay trucks showing that the hay on board has been Marked by Brindo.
The banner will be 52x91cm (landscape)
The banner needs to say "Marked by Brindo" using the company logo.
It also needs the website "www.brindo.com.au" displayed.
We have attached an image of our logo, the product itself and the back of a truck it will be attached to for reference.

```html
<!DOCTYPE html>
<html lang="en">
<head>
<meta charset="utf-8">
<title>Marked by Brindo – Truck Banner</title>
<link rel="stylesheet" href="https://fonts.googleapis.com/css2?family=Poppins:ital,wght@0,700;0,800;1,800;1,900&display=swap">
<style>
  :root {
    --stage: #5a5a5a;
    --paper: #f3f1f0;
    --paper-speck: #e2dfdd;
    --brown: #564a3f;
    --ink: #2a2a26;
    --orange: #f6ae42;
    --white: #ffffff;
  }
  * { margin: 0; padding: 0; box-sizing: border-box; }
  html, body {
    width: 1200px; height: 800px; overflow: hidden;
    background: var(--stage);
    font-family: "Poppins", sans-serif;
  }
  .banner {
    position: absolute; left: 40px; top: 80px;
    width: 1120px; height: 640px; overflow: hidden;
    background:
      radial-gradient(circle at 20% 30%, var(--paper-speck) 0 1px, transparent 2px) 0 0 / 23px 19px,
      radial-gradient(circle at 70% 60%, var(--paper-speck) 0 1px, transparent 2px) 0 0 / 31px 27px,
      var(--paper);
    box-shadow: 0 4px 12px rgba(0,0,0,.35);
  }
  .headline {
    position: absolute; left: 88px; top: 48px;
    font-weight: 900; font-style: italic; line-height: 1;
    letter-spacing: -2px;
  }
  .headline__marked { display: block; font-size: 132px; color: var(--brown); }
  .headline__by {
    display: block; font-size: 132px; color: var(--ink);
    margin-left: 190px; margin-top: -14px;
  }
  .brand-name {
    position: absolute; left: 112px; top: 268px;
    font-weight: 800; font-size: 150px; line-height: 1;
    color: var(--brown); letter-spacing: -3px;
  }
  .product-circle {
    position: absolute; left: 725px; top: 55px;
    width: 386px; height: 386px; border-radius: 50%;
    background: var(--orange);
  }
  .product-photo {
    position: absolute; left: 668px; top: 110px;
    width: 440px; height: 290px; border-radius: 10px;
    background: linear-gradient(160deg, #e4e6df 0%, #c9ccc4 60%, #8d8f8a 100%);
  }
  .footer-band { position: absolute; left: 0; top: 440px; width: 1120px; height: 200px; }
  .website {
    position: absolute; left: 0; right: 0; top: 505px;
    text-align: center; font-weight: 900; font-style: italic;
    font-size: 92px; line-height: 1; letter-spacing: -1px;
    color: var(--white);
  }
  .website__name { color: var(--orange); }
</style>
</head>
<body>
  <main class="banner">
    <h1 class="headline">
      <span class="headline__marked">MARKED</span>
      <span class="headline__by">BY</span>
    </h1>
    <div class="brand-name">Brindo</div>

    <div class="product-circle"></div>
    <div class="product-photo" role="img" aria-label="Photo of the Brindo bale tagging unit, a pale grey metal applicator with a blue air hose"></div>

    <svg class="footer-band" viewBox="0 0 1120 200" preserveAspectRatio="none" aria-hidden="true">
      <path fill="var(--ink)" d="M0 34 L20 28 L45 24 L70 26 L100 22 L140 25 L180 20 L220 18 L260 12 L300 16 L340 10 L380 8 L420 6 L460 4 L500 9 L540 7 L580 13 L620 15 L660 20 L700 17 L740 24 L780 22 L820 28 L860 26 L900 30 L940 27 L980 32 L1020 30 L1060 34 L1090 32 L1120 36 L1120 200 L0 200 Z"/>
    </svg>
    <p class="website">www.<span class="website__name">brindo</span>.com.au</p>
  </main>
</body>
</html>
```